Postcard needed for expert witness service

Looking for a professional postcard that will be mailed to personal injury lawyers / law firms to introduce my expert witness services.

Target Market(s)

Law firms, personal injury lawyers

Industry/Entity Type

Expert witness, law

Font styles to use
Sans Serif

Requirements
Must have
• Logo: The Frost Counsel [Main Heading]Do you handle snow and ice related slip and falls? Darrel is one of the top snow industry experts in the country! [Following should be in a list type fashion, possibly bulleted]Darrel's credentials: Accredited Winter Practitioner (AWP), past WRTA board member and chair, former ISO 9001 certified snow company owner , 32 years in the industry. (555) 284-3917 NOTES: Postcard will be 4" x 6" Please use both sides however must have room for labels and stamp
Should not have
• Wouldn't suggest using both photos on same side. Honestly, feel free to only use one of the slip and fall photos if it works out better. Thanks!

```html
<!DOCTYPE html>
<html lang="en">
<head>
<meta charset="utf-8">
<title>The Frost Counsel – Postcard</title>
<link rel="stylesheet" href="https://fonts.googleapis.com/css2?family=Poppins:wght@300;400;500;700;800&display=swap">
<style>
  :root {
    --backdrop: #8b9090;
    --card: #ffffff;
    --ink: #000000;
    --stamp: #e6e6e6;
    --photo-cool-a: #c9ccd0;
    --photo-cool-b: #5f7290;
    --photo-cool-c: #8d8f93;
    --photo-warm-a: #e9e9ea;
    --photo-warm-b: #5b4a44;
    --photo-warm-c: #4d5f7c;
  }
  * { box-sizing: border-box; margin: 0; padding: 0; }
  html, body { width: 1200px; height: 2400px; overflow: hidden; }
  body {
    background: var(--backdrop);
    font-family: "Poppins", sans-serif;
    color: var(--ink);
    position: relative;
  }
  .postcard {
    position: absolute;
    left: 86px;
    width: 1028px;
    height: 686px;
    background: var(--card);
    overflow: hidden;
    box-shadow: 0 2px 6px rgba(0,0,0,0.25);
  }
  .postcard--front { top: 487px; }
  .postcard--back { top: 1226px; }

  /* Front */
  .front-photo {
    position: absolute; left: 0; top: 0; width: 508px; height: 100%;
    background: linear-gradient(160deg, var(--photo-cool-a) 0%, var(--photo-cool-b) 45%, var(--photo-cool-c) 100%);
  }
  .headline {
    position: absolute; right: 30px; top: 50px; width: 528px; text-align: right;
  }
  .headline__lead {
    font-weight: 800; font-size: 40px; line-height: 48px; letter-spacing: -1px; margin-bottom: 5px;
  }
  .headline__bar {
    display: block; background: var(--ink); color: var(--card);
    font-weight: 800; font-size: 62px; line-height: 58px; height: 58px;
    padding-right: 22px; letter-spacing: -1.5px; margin-bottom: 10px;
  }
  .tagline {
    position: absolute; right: 40px; top: 309px; text-align: right;
    font-size: 26px; line-height: 34px; font-weight: 400; text-transform: uppercase;
  }
  .brand {
    display: flex; flex-direction: column; align-items: stretch; text-transform: uppercase;
  }
  .brand__name { font-weight: 300; font-size: 36px; line-height: 36px; letter-spacing: 0.5px; text-align: center; }
  .brand__sub {
    display: flex; align-items: center; gap: 10px;
    font-weight: 400; font-size: 16px; letter-spacing: 4px; line-height: 18px;
  }
  .brand__sub::before, .brand__sub::after { content: ""; flex: 1; height: 2px; background: var(--ink); }
  .postcard--front .brand { position: absolute; right: 40px; top: 586px; }

  /* Back */
  .credentials { position: absolute; left: 40px; top: 42px; width: 587px; }
  .credentials__title {
    font-weight: 800; font-size: 30px; line-height: 36px; letter-spacing: -0.3px;
    padding-bottom: 6px; border-bottom: 1.5px solid var(--ink);
  }
  .credentials__list { list-style: none; margin-top: 12px; }
  .credentials__list li {
    font-size: 23px; line-height: 38px; font-weight: 400; display: flex; align-items: center; gap: 12px;
  }
  .credentials__list li::before {
    content: ""; width: 0; height: 0;
    border-top: 6px solid transparent; border-bottom: 6px solid transparent; border-left: 9px solid var(--ink);
  }
  .phone {
    position: absolute; left: 39px; top: 266px; width: 317px; height: 58px;
    background: var(--ink); color: var(--card);
    display: flex; align-items: center; justify-content: center; gap: 10px;
    font-weight: 700; font-size: 32px; letter-spacing: 0.5px;
  }
  .phone svg { width: 26px; height: 26px; }
  .postcard--back .brand { position: absolute; left: 427px; top: 272px; width: 196px; }
  .postcard--back .brand__name { font-size: 34px; line-height: 34px; }
  .postcard--back .brand__sub { font-size: 15px; letter-spacing: 3.5px; }
  .back-photo {
    position: absolute; left: 0; top: 360px; width: 644px; height: 326px;
    background: linear-gradient(200deg, var(--photo-warm-a) 0%, var(--photo-warm-b) 45%, var(--photo-warm-c) 100%);
  }
  .stamp-area { position: absolute; left: 887px; top: 41px; width: 102px; height: 102px; background: var(--stamp); }
</style>
</head>
<body>
  <section class="postcard postcard--front">
    <div class="front-photo" role="img" aria-label="Photo of a person slipping backwards on an icy sidewalk, backpack falling to the ground"></div>
    <h1 class="headline">
      <span class="headline__lead">DO YOU HANDLE</span>
      <span class="headline__bar">SNOW &amp; ICE</span>
      <span class="headline__bar">RELATED SLIP</span>
      <span class="headline__bar">AND FALLS?</span>
    </h1>
    <p class="tagline">Darrel is one of the<br>top snow industry experts<br>in the country!</p>
    <div class="brand">
      <span class="brand__name">The Frost Counsel</span>
    </div>
  </section>

  <section class="postcard postcard--back">
    <div class="credentials">
      <h2 class="credentials__title">DARREL'S CREDENTIALS</h2>
      <ul class="credentials__list">
        <li>Accredited Winter Practitioner (AWP)</li>
        <li>Past WRTA board member and chair</li>
        <li>Former ISO 9001 certified snow company owner</li>
        <li>32 years in the industry.</li>
      </ul>
    </div>
    <div class="phone">
      <svg viewBox="0 0 24 24" aria-hidden="true"><path fill="#fff" d="M6.6 10.8c1.4 2.8 3.8 5.1 6.6 6.6l2.2-2.2c.3-.3.7-.4 1-.2 1.1.4 2.3.6 3.6.6.6 0 1 .4 1 1V20c0 .6-.4 1-1 1C10.6 21 3 13.4 3 4c0-.6.4-1 1-1h3.5c.6 0 1 .4 1 1 0 1.3.2 2.5.6 3.6.1.3 0 .7-.2 1l-2.3 2.2z"/></svg>
      <span>(555) 284-3917</span>
    </div>
    <div class="brand">
      <span class="brand__name">The Frost Counsel</span>
    </div>
    <div class="back-photo" role="img" aria-label="Photo of a woman in a winter coat and knit hat who has fallen on a snowy, icy path"></div>
    <div class="stamp-area" aria-label="Stamp area"></div>
  </section>
</body>
</html>
```